Civil engineering company | Billboard

We need a billboard design for Velmora- civil engineering company. We want big logo in the center of billboard and web site (www.velmora.hr) below the logo. Also, we want an subtle abstract pattern in the background. Dimensions of the billboard are: width :10 m, height: 2m. Design must be celan and modern.
Industry/Entity Type
Civil engineering
Font styles to use
Sans Serif
Colors
F0912C
F2A743
F7CA91
FBE8D2
FDF5EE
Requirements
Must have
- Logo and new unique pattern design for Velmroa company
Should not have
- pictures of construction machinery and tools

```html
<!DOCTYPE html>
<html lang="hr">
<head>
<meta charset="utf-8">
<title>Velmora – billboard</title>
<link rel="stylesheet" href="https://fonts.googleapis.com/css2?family=Montserrat:wght@500;600;700&display=swap">
<style>
  :root {
    --page: #ffffff;
    --board-dark: #262422;
    --board-deep: #15171c;
    --site-tone: #3a332b;
    --orange: #e08e34;
    --white: #ffffff;
    --ink: #1a1714;
  }
  html, body {
    margin: 0;
    padding: 0;
    width: 1020px;
    height: 1200px;
    overflow: hidden;
    background: var(--page);
  }
  .canvas {
    position: relative;
    width: 1020px;
    height: 1200px;
  }
  .billboard {
    position: absolute;
    left: 30px;
    top: 504px;
    width: 960px;
    height: 192px;
    box-shadow: 0 18px 40px rgba(0, 0, 0, 0.35);
  }
  .billboard svg { display: block; }
  .brand-name {
    font-family: "Montserrat", sans-serif;
    font-weight: 600;
    font-size: 44px;
    letter-spacing: 2px;
    fill: var(--orange);
  }
  .tagline {
    font-family: "Montserrat", sans-serif;
    font-weight: 600;
    font-size: 12.5px;
    fill: var(--white);
  }
  .web-address {
    font-family: "Montserrat", sans-serif;
    font-weight: 700;
    font-size: 30px;
    letter-spacing: 12px;
    fill: var(--ink);
  }
</style>
</head>
<body>
<main class="canvas">
  <section class="billboard" aria-label="Velmora billboard">
    <svg width="960" height="192" viewBox="0 0 960 192" xmlns="http://www.w3.org/2000/svg">
      <defs>
        <linearGradient id="board-bg" x1="0" y1="0" x2="1" y2="0">
          <stop offset="0" stop-color="var(--board-dark)"/>
          <stop offset="0.6" stop-color="var(--board-dark)"/>
          <stop offset="1" stop-color="var(--board-deep)"/>
        </linearGradient>
        <radialGradient id="site-glow" cx="0.5" cy="0.45" r="0.5">
          <stop offset="0" stop-color="var(--site-tone)" stop-opacity="0.7"/>
          <stop offset="1" stop-color="var(--site-tone)" stop-opacity="0"/>
        </radialGradient>
      </defs>

      <rect class="board-base" width="960" height="192" fill="url(#board-bg)"/>
      <rect class="site-photo" x="220" y="0" width="700" height="180" fill="url(#site-glow)"
            role="img" aria-label="Faint photo of a building site with crane and scaffolding"/>

      <g class="logo">
        <rect class="logo-square" x="293" y="51" width="57" height="57" fill="none" stroke="var(--white)" stroke-width="2"/>
        <text class="brand-name" x="366" y="93">VELMORA</text>
      </g>
      <text class="tagline" x="366" y="113" textLength="343" lengthAdjust="spacingAndGlyphs">IZVOĐENJE I VOĐENJE GRAĐEVINSKIH RADOVA</text>

      <g class="web-band">
        <polygon points="160,140 817,140 834,188 136,188" fill="var(--orange)"/>
        <polygon points="160,140 176,140 152,188 136,188" fill="var(--white)" opacity="0"/>
        <polygon points="167,140 177,140 155,186 145,186" fill="var(--white)"/>
        <polygon points="800,140 810,140 827,186 817,186" fill="var(--white)"/>
        <rect class="base-line" x="0" y="186" width="960" height="4" fill="var(--orange)"/>
        <text class="web-address" x="484" y="176" text-anchor="middle">www.velmora.hr</text>
      </g>
    </svg>
  </section>
</main>
</body>
</html>
```